Health software company called BRIGHT HARBOR, committed to innovation and technological excellence

The powerpoint presentation template is necessary, very necessary is elegant and modern with innovative images and the color palette attached. The presentation will be used for the business plan and investor presentations that we will use to raise funds. Please, recommend a modern typeface, as well as format to be able to use it and incorporate it as part of the company's brand guidelines. Great diversity of technological solutions

Very low attendance of designers for a high budget. Very few proposals and no capture my interest

Target Market(s)

managers, managers of public and private health centers, government states, investors

Industry/Entity Type

It Company

Font styles to use
Serif

Requirements
Must have
• The powerpoint presentation template is necessary, very necessary is elegant, minimalist and modern with innovative images and the color palette attached. it must be refined in demarcated style
Nice to have
• very nice, visually harmonic avoid saturation
Should not have
• NO dark colors NO dark colors NO dark colors NO dark colors NO dark colors

```html
<!DOCTYPE html>
<html lang="en">
<head>
<meta charset="utf-8">
<title>Bright Harbor – Business Plan Template</title>
<link rel="stylesheet" href="https://fonts.googleapis.com/css2?family=Montserrat:wght@400;500;600;700&display=swap">
<style>
:root{
  --cyan:#3fe9ee;
  --teal:#36e2cf;
  --blue:#2d7ff9;
  --title:#3b8ff5;
  --ink:#333;
  --muted:#8a8a8a;
  --line:#dcdcdc;
  --canvas:#f3f3f3;
  --hero-a:#5ff2f8;
  --hero-b:#2b9cf3;
}
*{box-sizing:border-box;margin:0;padding:0}
html,body{width:1200px;height:798px;overflow:hidden;background:var(--canvas);font-family:"Montserrat",sans-serif;color:var(--ink)}
.deck{position:relative;width:1200px;height:798px}
.slide{position:absolute;width:273px;height:156px;background:#fff;border:1px solid var(--line);overflow:hidden}
.num{position:absolute;font-size:14px;color:#777;font-weight:500}
.abs{position:absolute}
.hero{background:linear-gradient(115deg,var(--hero-a) 0%,#45c8f6 50%,var(--hero-b) 100%)}
.photo{position:absolute;inset:0;background:linear-gradient(120deg,rgba(255,255,255,.18),rgba(255,255,255,0) 55%,rgba(20,90,200,.18))}
.title{position:absolute;left:22px;top:14px;font-size:12.5px;color:var(--title);font-weight:500;letter-spacing:.2px}
.summary{position:absolute;left:22px;top:29px;font-size:4.5px;color:var(--muted)}
.tiny{font-size:3.8px;line-height:5px;color:var(--muted)}
.brand{position:absolute;left:50%;transform:translateX(-50%);display:flex;align-items:center;gap:4px;color:#fff;font-size:7px;font-weight:600;letter-spacing:1px;white-space:nowrap}
.brand i{display:block;width:8px;height:8px;border:1px solid #fff}
.hero-title{position:absolute;left:0;right:0;text-align:center;color:#fff;font-weight:700}
.circle{position:absolute;width:48px;height:48px;border-radius:50%;border:1.5px solid var(--cyan);display:flex;align-items:center;justify-content:center;font-size:5.5px;font-weight:700;color:#444}
.circle.blue{border-color:var(--blue)}
.caption{position:absolute;width:58px;text-align:center}
.stat{position:absolute;width:91px;text-align:center}
.stat b{display:block;color:var(--blue);font-size:10px;margin-bottom:8px}
.item{position:absolute;display:flex;align-items:flex-start;gap:3px}
.item .n{color:var(--teal);font-weight:700;font-size:9px;width:8px;line-height:9px}
.item .n.blue{color:var(--blue)}
.item .txt{border-left:1px solid var(--line);padding-left:3px;font-size:4.2px;line-height:5px;color:var(--muted)}
.item .txt strong{display:block;color:#222;font-size:4.2px}
.swot{position:absolute;width:56px;text-align:center}
.swot .dot{width:26px;height:26px;border-radius:50%;margin:0 auto;display:flex;align-items:center;justify-content:center;color:#fff;font-weight:700;font-size:12px;background:var(--teal)}
.swot .dot.blue{background:var(--blue)}
.swot h4{font-size:4.6px;margin:8px 0 5px;font-weight:700}
.swot ul{font-size:4px;line-height:5px;color:#555;text-align:left;padding-left:12px}
.member{position:absolute;width:39px;height:39px;display:flex;flex-direction:column;align-items:center;justify-content:center;color:#fff;font-size:4.6px;text-align:center;line-height:5px}
.member span{font-size:3.4px;opacity:.8}
table.returns{position:absolute;left:23px;top:50px;width:230px;border-collapse:collapse;font-size:3.4px}
table.returns th{background:var(--blue);color:#fff;font-weight:700;height:11px;padding:0 2px}
table.returns td{height:12.3px;color:#888;padding-left:3px}
table.returns tr:nth-child(even) td{background:#f1f1f1}
.col{position:absolute;top:36px;width:70px;font-size:3.6px;line-height:5.2px;color:#777;text-align:justify}
</style>
</head>
<body>
<main class="deck">

<!-- 1 -->
<section class="slide hero" style="left:18px;top:10px">
  <div class="photo" role="img" aria-label="Soft photo of medical technology in blue tones"></div>
  <div class="brand" style="top:46px"><i></i>BRIGHT HARBOR</div>
  <div class="hero-title" style="top:98px;font-size:14px">BUSINESS PLAN</div>
  <div class="abs" style="left:70px;top:116px;width:126px;height:1px;background:#fff"></div>
  <div class="hero-title" style="top:122px;font-size:6px;font-weight:400;line-height:8px">COMMITTED TO INNOVATION AND<br>TECHNOLOGICAL EXCELLENCE</div>
</section>
<div class="num" style="left:20px;top:172px">1</div>

<!-- 2 -->
<section class="slide" style="left:317px;top:10px">
  <div class="title">MISSION, VISION, VALUE</div>
  <div class="summary">Add some summary text here to reinforce your points.</div>
  <div class="abs" style="left:92px;top:71px;width:20px;height:1px;background:var(--line)"></div>
  <div class="abs" style="left:161px;top:71px;width:20px;height:1px;background:var(--line)"></div>
  <div class="circle" style="left:44px;top:47px">MISSION</div>
  <div class="circle" style="left:113px;top:47px">VISION</div>
  <div class="circle blue" style="left:182px;top:47px">VALUE</div>
  <div class="caption tiny" style="left:39px;top:104px">Refers to a good or service being offered by a company. Ideally, a product should meet a certain consumer demand.</div>
  <div class="caption tiny" style="left:108px;top:104px">Refers to a good or service being offered by a company. Ideally, a product should meet a certain consumer demand.</div>
  <div class="caption tiny" style="left:177px;top:104px">Refers to a good or service being offered by a company. Ideally, a product should meet a certain consumer demand.</div>
</section>
<div class="num" style="left:319px;top:172px">2</div>

<!-- 3 -->
<section class="slide" style="left:615px;top:10px">
  <div class="title" style="top:20px">MARKET RESEARCH</div>
  <div class="summary" style="top:35px">Add some summary text here to reinforce your points.</div>
  <svg class="abs" style="left:0;top:0" width="273" height="156" viewBox="0 0 273 156">
    <g fill="none" stroke-width="6">
      <circle cx="55" cy="92" r="30" stroke="#efefef"/>
      <circle cx="55" cy="92" r="30" stroke="var(--cyan)" stroke-dasharray="84.8 200" transform="rotate(-90 55 92)"/>
      <circle cx="138" cy="92" r="30" stroke="#efefef"/>
      <circle cx="138" cy="92" r="30" stroke="var(--blue)" stroke-dasharray="84.8 200" transform="rotate(-90 138 92)"/>
      <circle cx="221" cy="92" r="30" stroke="#efefef"/>
      <circle cx="221" cy="92" r="30" stroke="var(--cyan)" stroke-dasharray="141.4 200" transform="rotate(-90 221 92)"/>
    </g>
    <g font-family="Montserrat, sans-serif" text-anchor="middle">
      <text x="55" y="88" font-size="7" font-weight="700" fill="#444">45%</text>
      <text x="138" y="88" font-size="7" font-weight="700" fill="#444">45%</text>
      <text x="221" y="88" font-size="7" font-weight="700" fill="#444">75%</text>
      <g font-size="4" fill="#999">
        <text x="55" y="94">of the</text><text x="55" y="99">market is</text><text x="55" y="104">something</text><text x="55" y="109">meaningful</text>
        <text x="138" y="94">of the</text><text x="138" y="99">market is</text><text x="138" y="104">something</text><text x="138" y="109">meaningful</text>
        <text x="221" y="94">of the</text><text x="221" y="99">market is</text><text x="221" y="104">something</text><text x="221" y="109">meaningful</text>
      </g>
    </g>
  </svg>
</section>
<div class="num" style="left:617px;top:172px">3</div>

<!-- 4 -->
<section class="slide hero" style="left:914px;top:10px">
  <div class="photo" role="img" aria-label="Soft background photo of a clinic in blue tones"></div>
  <div class="hero-title" style="top:64px;font-size:11px">MARKET RESEARCH QUOTE</div>
  <div class="hero-title" style="top:88px;font-size:5.6px;font-weight:400;line-height:7px;opacity:.85">A PRODUCT LIKE THIS IS SO IMPORTANT TO ME. IT<br>WILL HELP ME ACHIEVE X, Y, Z.</div>
  <div class="hero-title" style="top:110px;font-size:4px;font-weight:400;opacity:.8">NAME, COMPANY</div>
</section>
<div class="num" style="left:916px;top:172px">4</div>

<!-- 5 -->
<section class="slide" style="left:18px;top:212px">
  <div class="abs hero" style="left:0;top:0;width:273px;height:87px">
    <div class="photo" role="img" aria-label="Photo of a health professional with data overlay in cyan tones"></div>
    <div class="hero-title" style="top:43px;font-size:11px">IMPORTANT STATEMENT</div>
  </div>
  <div class="abs" style="left:91px;top:87px;width:1px;height:69px;background:var(--line)"></div>
  <div class="abs" style="left:182px;top:87px;width:1px;height:69px;background:var(--line)"></div>
  <div class="stat tiny" style="left:0;top:105px"><b>45%</b>of the market is<br>something<br>meaningful.</div>
  <div class="stat tiny" style="left:91px;top:105px"><b>25%</b>of the market is<br>something<br>meaningful.</div>
  <div class="stat tiny" style="left:182px;top:105px"><b>77%</b>of the market is<br>something<br>meaningful.</div>
</section>
<div class="num" style="left:20px;top:374px">5</div>

<!-- 6 -->
<section class="slide" style="left:317px;top:212px">
  <div class="abs hero" style="left:3px;top:3px;width:118px;height:150px" role="img" aria-label="Photo of a person with a digital health interface in blue tones"></div>
  <div class="title" style="left:145px;top:12px;font-size:11px">LIST OF 4 ITEMS</div>
  <div class="summary" style="left:145px;top:25px;line-height:6px">Add some summary text here to<br>reinforce your points.</div>
  <div class="item" style="left:149px;top:48px"><div class="n">1</div><div class="txt">Add some summary text here to<br>reinforce your points.</div></div>
  <div class="item" style="left:149px;top:75px"><div class="n">2</div><div class="txt">Add some summary text here to<br>reinforce your points.</div></div>
  <div class="item" style="left:149px;top:102px"><div class="n blue">3</div><div class="txt">Add some summary text here to<br>reinforce your points.</div></div>
  <div class="item" style="left:149px;top:128px"><div class="n">4</div><div class="txt">Add some summary text here to<br>reinforce your points.</div></div>
</section>
<div class="num" style="left:319px;top:374px">6</div>

<!-- 7 -->
<section class="slide" style="left:615px;top:212px">
  <div class="title" style="left:22px;top:12px;font-size:10px">LIST OF 8 ITEMS</div>
  <div class="summary" style="top:25px">Add some summary text here to reinforce your points.</div>
  <div class="item" style="left:27px;top:45px"><div class="n">1</div><div class="txt"><strong>POINT 1</strong>Add some summary text here<br>to reinforce your points.</div></div>
  <div class="item" style="left:27px;top:71px"><div class="n">2</div><div class="txt"><strong>POINT 2</strong>Add some summary text here<br>to reinforce your points.</div></div>
  <div class="item" style="left:27px;top:98px"><div class="n blue">3</div><div class="txt"><strong>POINT 3</strong>Add some summary text here<br>to reinforce your points.</div></div>
  <div class="item" style="left:27px;top:124px"><div class="n">4</div><div class="txt"><strong>POINT 4</strong>Add some summary text here<br>to reinforce your points.</div></div>
  <div class="item" style="left:151px;top:45px"><div class="n">5</div><div class="txt"><strong>POINT 5</strong>Add some summary text here<br>to reinforce your points.</div></div>
  <div class="item" style="left:151px;top:71px"><div class="n">6</div><div class="txt"><strong>POINT 6</strong>Add some summary text here<br>to reinforce your points.</div></div>
  <div class="item" style="left:151px;top:98px"><div class="n blue">7</div><div class="txt"><strong>POINT 7</strong>Add some summary text here<br>to reinforce your points.</div></div>
  <div class="item" style="left:151px;top:124px"><div class="n">8</div><div class="txt"><strong>POINT 8</strong>Add some summary text here<br>to reinforce your points.</div></div>
</section>
<div class="num" style="left:617px;top:374px">7</div>

<!-- 8 -->
<section class="slide" style="left:914px;top:212px">
  <div class="title" style="left:23px;top:18px">PIE CHART</div>
  <div class="abs" style="left:38px;top:55px;font-size:8.5px;line-height:10.5px;color:#333;width:90px">Make a great point about the data represented in the enclosed pie chart here.</div>
  <svg class="abs" style="left:0;top:0" width="273" height="156" viewBox="0 0 273 156">
    <g fill="none" stroke-width="9" transform="rotate(-90 188 80)">
      <circle cx="188" cy="80" r="37" stroke="var(--cyan)"/>
      <circle cx="188" cy="80" r="37" stroke="var(--blue)" stroke-dasharray="22 300" stroke-dashoffset="50"/>
      <circle cx="188" cy="80" r="37" stroke="var(--teal)" stroke-dasharray="10 300" stroke-dashoffset="28"/>
    </g>
    <text x="188" y="82" text-anchor="middle" font-family="Montserrat, sans-serif" font-size="5" font-weight="700" fill="#444">CHART TITLE</text>
    <g font-family="Montserrat, sans-serif" font-size="3.8" fill="#999">
      <circle cx="151" cy="130" r="1.3" fill="var(--cyan)"/><text x="154" y="131.5">1st Qtr</text>
      <circle cx="171" cy="130" r="1.3" fill="var(--teal)"/><text x="174" y="131.5">2nd Qtr</text>
      <circle cx="192" cy="130" r="1.3" fill="var(--blue)"/><text x="195" y="131.5">3rd Qtr</text>
      <circle cx="212" cy="130" r="1.3" fill="var(--cyan)"/><text x="215" y="131.5">4th Qtr</text>
    </g>
  </svg>
</section>
<div class="num" style="left:916px;top:374px">8</div>

<!-- 9 -->
<section class="slide" style="left:18px;top:414px">
  <div class="title" style="left:23px;top:18px">BAR CHART</div>
  <svg class="abs" style="left:0;top:0" width="273" height="156" viewBox="0 0 273 156">
    <line x1="46" y1="114" x2="230" y2="114" stroke="#ddd" stroke-width=".6"/>
    <g>
      <rect x="53" y="58.8" width="8" height="55.2" fill="var(--teal)"/>
      <rect x="62" y="62.4" width="8" height="51.6" fill="var(--cyan)"/>
      <rect x="71" y="91.2" width="8" height="22.8" fill="var(--blue)"/>
      <rect x="99" y="94.8" width="8" height="19.2" fill="var(--teal)"/>
      <rect x="108" y="90" width="8" height="24" fill="var(--cyan)"/>
      <rect x="117" y="96" width="8" height="18" fill="var(--blue)"/>
      <rect x="146" y="105.6" width="8" height="8.4" fill="var(--teal)"/>
      <rect x="155" y="90" width="8" height="24" fill="var(--cyan)"/>
      <rect x="164" y="54" width="8" height="60" fill="var(--blue)"/>
      <rect x="192" y="105" width="8" height="9" fill="var(--teal)"/>
      <rect x="201" y="72" width="8" height="42" fill="var(--cyan)"/>
      <rect x="210" y="66" width="8" height="48" fill="var(--blue)"/>
    </g>
    <g font-family="Montserrat, sans-serif" font-size="3" fill="#666" text-anchor="middle">
      <text x="57" y="57">9.2</text><text x="66" y="61">8.6</text><text x="75" y="90">3.8</text>
      <text x="103" y="93">3.2</text><text x="112" y="89">4.0</text><text x="121" y="95">3.0</text>
      <text x="150" y="104">1.4</text><text x="159" y="89">4.0</text><text x="168" y="53">10.0</text>
      <text x="196" y="104">1.5</text><text x="205" y="71">7.0</text><text x="214" y="65">8.0</text>
    </g>
    <g font-family="Montserrat, sans-serif" font-size="3.4" fill="#999" text-anchor="middle">
      <text x="66" y="120">1st Qtr</text><text x="112" y="120">2nd Qtr</text><text x="159" y="120">3rd Qtr</text><text x="205" y="120">4th Qtr</text>
    </g>
    <g font-family="Montserrat, sans-serif" font-size="3.8" fill="#999">
      <circle cx="112" cy="124" r="1.2" fill="var(--teal)"/><text x="114.5" y="125.5">Sales</text>
      <circle cx="129" cy="124" r="1.2" fill="var(--cyan)"/><text x="131.5" y="125.5">Sales1</text>
      <circle cx="148" cy="124" r="1.2" fill="var(--blue)"/><text x="150.5" y="125.5">Sales2</text>
    </g>
  </svg>
</section>
<div class="num" style="left:20px;top:576px">9</div>

<!-- 10 -->
<section class="slide" style="left:317px;top:414px">
  <div class="title" style="left:22px;top:18px">STRATEGY</div>
  <div class="summary" style="top:33px">Add some summary text here to reinforce your points.</div>
  <svg class="abs" style="left:0;top:0" width="273" height="156" viewBox="0 0 273 156">
    <path d="M76 55 Q122 87 76 119" fill="none" stroke="#e8f8fb" stroke-width="8"/>
    <rect x="0" y="74" width="84" height="26" fill="var(--cyan)"/>
    <circle cx="72" cy="87" r="11" fill="#fff"/>
    <circle cx="72" cy="87" r="8" fill="var(--cyan)"/>
    <circle cx="72" cy="87" r="4" fill="none" stroke="#fff" stroke-width="1.2"/>
    <g stroke="#fff" stroke-width="1.2"><line x1="72" y1="79" x2="72" y2="83"/><line x1="72" y1="91" x2="72" y2="95"/><line x1="64" y1="87" x2="68" y2="87"/><line x1="76" y1="87" x2="80" y2="87"/></g>
    <text x="14" y="89.5" font-family="Montserrat, sans-serif" font-size="6.5" font-weight="700" fill="#fff">STRATEGY</text>
    <circle cx="77" cy="56" r="4.5" fill="var(--cyan)"/>
    <circle cx="107" cy="87" r="4.5" fill="var(--cyan)"/>
    <circle cx="77" cy="118" r="4.5" fill="var(--cyan)"/>
  </svg>
  <div class="abs" style="left:88px;top:51px;font-size:6px;color:#222">STRATEGIC OBJECTIVE 1</div>
  <div class="abs tiny" style="left:88px;top:59px;width:110px">Add a little clarifying text here. It doesn't have to be more than 1-2 sentences.</div>
  <div class="abs" style="left:116px;top:82px;font-size:6px;color:#222">STRATEGIC OBJECTIVE 2</div>
  <div class="abs tiny" style="left:116px;top:90px;width:82px">Add a little clarifying text here. It doesn't have to be more than 1-2 sentences.</div>
  <div class="abs" style="left:88px;top:113px;font-size:6px;color:#222">STRATEGIC OBJECTIVE 3</div>
  <div class="abs tiny" style="left:88px;top:121px;width:128px">Add a little clarifying text here. It doesn't have to be more than 1-2 sentences.</div>
</section>
<div class="num" style="left:319px;top:576px">10</div>

<!-- 11 -->
<section class="slide" style="left:615px;top:414px">
  <div class="title" style="left:22px;top:16px">FINANCING</div>
  <div class="summary" style="top:30px">Add some summary text here to reinforce your points.</div>
  <div class="abs" style="left:3px;top:41px;width:135px;height:96px;background:var(--blue);color:#fff;text-align:center">
    <div style="font-size:20px;font-weight:700;margin-top:26px">$1M</div>
    <div style="font-size:8px;margin-top:2px">EQUITY FINANCING</div>
    <div style="font-size:7px">15%</div>
  </div>
  <div class="item" style="left:153px;top:42px"><div class="n">1</div><div class="txt"><strong>USE OF FUNDING 1</strong>Add some summary text here<br>to reinforce your points.</div></div>
  <div class="item" style="left:153px;top:68px"><div class="n">2</div><div class="txt"><strong>USE OF FUNDING 2</strong>Add some summary text here<br>to reinforce your points.</div></div>
  <div class="item" style="left:153px;top:95px"><div class="n blue">3</div><div class="txt"><strong>USE OF FUNDING 3</strong>Add some summary text here<br>to reinforce your points.</div></div>
  <div class="item" style="left:153px;top:121px"><div class="n">4</div><div class="txt"><strong>USE OF FUNDING 4</strong>Add some summary text here<br>to reinforce your points.</div></div>
</section>
<div class="num" style="left:617px;top:576px">11</div>

<!-- 12 -->
<section class="slide" style="left:914px;top:414px">
  <div class="title" style="left:23px;top:18px">EXIT &amp; RETURNS</div>
  <div class="summary" style="left:23px;top:32px">Add some summary text here to reinforce your points.</div>
  <table class="returns">
    <tr><th>SHAREHOLDER</th><th>SHARES</th><th>PRE-MONEY<br>VALUATION</th><th>POST-MONEY<br>VALUATION</th><th>RETURN AT<br>3X</th><th>RETURN AT<br>5X</th><th>RETURN AT<br>10X</th></tr>
    <tr><td>NAME 1</td><td></td><td></td><td></td><td></td><td></td><td></td></tr>
    <tr><td>NAME 2</td><td></td><td></td><td></td><td></td><td></td><td></td></tr>
    <tr><td>NAME 3</td><td></td><td></td><td></td><td></td><td></td><td></td></tr>
    <tr><td>NAME 4</td><td></td><td></td><td></td><td></td><td></td><td></td></tr>
    <tr><td>NAME 5</td><td></td><td></td><td></td><td></td><td></td><td></td></tr>
    <tr><td>NAME 6</td><td></td><td></td><td></td><td></td><td></td><td></td></tr>
  </table>
</section>
<div class="num" style="left:916px;top:576px">12</div>

<!-- 13 -->
<section class="slide" style="left:18px;top:615px">
  <div class="title" style="left:18px;top:10px">SWOT ANALYSIS</div>
  <div class="abs" style="left:78px;top:44px;width:1px;height:78px;background:var(--line)"></div>
  <div class="abs" style="left:137px;top:44px;width:1px;height:78px;background:var(--line)"></div>
  <div class="abs" style="left:195px;top:44px;width:1px;height:78px;background:var(--line)"></div>
  <div class="swot" style="left:20px;top:44px"><div class="dot">S</div><h4>STRENGTHS</h4><ul><li>Strength 1</li><li>Strength 2</li><li>Strength 3</li><li>Strength 4</li></ul></div>
  <div class="swot" style="left:79px;top:44px"><div class="dot">W</div><h4>WEAKNESSES</h4><ul><li>Weakness 1</li><li>Weakness 2</li><li>Weakness 3</li><li>Weakness 4</li></ul></div>
  <div class="swot" style="left:138px;top:44px"><div class="dot blue">O</div><h4>OPPORTUNITIES</h4><ul><li>Opportunities 1</li><li>Opportunities 2</li><li>Opportunities 3</li><li>Opportunities 4</li></ul></div>
  <div class="swot" style="left:196px;top:44px"><div class="dot">T</div><h4>THREATS</h4><ul><li>Threats 1</li><li>Threats 2</li><li>Threats 3</li><li>Threats 4</li></ul></div>
</section>
<div class="num" style="left:20px;top:777px">13</div>

<!-- 14 -->
<section class="slide" style="left:317px;top:615px">
  <div class="title" style="left:22px;top:10px">OUR TEAM</div>
  <div class="summary" style="top:25px">Add some summary text here to reinforce your points.</div>
  <div class="member" style="left:61px;top:48px;background:var(--teal)">Mia Lane<span>Manager<br>Assistant</span></div>
  <div class="member" style="left:141px;top:48px;background:var(--teal)">Mia Lane<span>Manager<br>Assistant</span></div>
  <div class="member" style="left:220px;top:48px;background:var(--cyan)">Alex Reed<span>Manager<br>Assistant</span></div>
  <div class="member" style="left:21px;top:87px;background:var(--cyan)">Alex Reed<span>Manager<br>Assistant</span></div>
  <div class="member" style="left:101px;top:87px;background:var(--blue)">Alex Reed<span>Manager<br>Assistant</span></div>
  <div class="member" style="left:180px;top:87px;background:var(--blue)">Alex Reed<span>Manager<br>Assistant</span></div>
</section>
<div class="num" style="left:319px;top:777px">14</div>

<!-- 15 -->
<section class="slide" style="left:615px;top:615px">
  <div class="title" style="left:22px;top:10px">TEXT-ONLY SLIDE</div>
  <div class="col" style="left:22px">Refers to a good or service being offered by a company. Ideally, a product should meet a certain consumer demand, or it should be so compelling that consumers believe they need it. Business executives should have a plan for dealing with products at every stage of their life cycles. Marketers must link the price to the real and perceived value of the product.<br><br>Place decisions outline where the product is sold and how it is delivered to the market. The goal of business executives is to get their products</div>
  <div class="col" style="left:102px">Refers to a good or service being offered by a company. Ideally, a product should meet a certain consumer demand, or it should be so compelling that consumers believe they need it. Business executives should value of the product, but they also must take into account supply costs, seasonal discounts, and prices used by competitors. Place decisions outline where the product is sold and how it is delivered to the market. The goal of business executives is to get their products in front of the consumers who are most likely to buy them.</div>
  <div class="col" style="left:182px">Refers to a good or service being offered by a company. Ideally, a product should meet a certain consumer demand, or it should be so compelling that consumers believe they need it. Business executives should have a plan for dealing with products at every stage of their life cycles.</div>
</section>
<div class="num" style="left:617px;top:777px">15</div>

<!-- 16 -->
<section class="slide hero" style="left:914px;top:615px">
  <div class="photo" role="img" aria-label="Soft photo of medical technology in blue tones"></div>
  <div class="brand" style="top:50px"><i></i>BRIGHT HARBOR</div>
  <div class="hero-title" style="top:94px;font-size:17px">THANK YOU</div>
</section>
<div class="num" style="left:916px;top:777px">16</div>

</main>
</body>
</html>
```